Restaurant service company needs a website!

I am looking for a skilled web designer/developer to create a professional, responsive, and easy-to-navigate website for my company, which specializes in servicing restaurant cooking equipment. The site should communicate trust, reliability, and technical expertise to our target audience, restaurant owners, managers, and commercial kitchen operators. I have included the company logos, if any other format for them is needed please let me know.

Target Market(s)

restaurant owners, managers, and commercial kitchen operators

Industry/Entity Type

Commercial Kitchen Equipment Service

Coding

Coded - Design and coding required

Number of Pages Required

1 page

Font styles to use
Serif
Sans Serif

Requirements
Must have
• Contact and service request forms, Click-to-call functionality for mobile, Clean, modern layout with strong visuals, Easy navigation, mobile-friendly
Nice to have
• Testimonials or Reviews, If possible a click-to-text functionality for mobile.
Should not have
• Any mention of Refrigeration or HVAC, "Free Quotes"

```html
<!DOCTYPE html>
<html lang="en">
<head>
<meta charset="utf-8">
<title>Waypoint Restaurant Service</title>
<link href="https://fonts.googleapis.com/css2?family=Archivo:wght@500;600;700;800&family=Mulish:wght@400;500;600;700;800&display=swap" rel="stylesheet">
<style>
:root{
  --teal:#0e5672;
  --teal-dark:#0a4660;
  --accent:#1c8cc8;
  --pale:#e3eef1;
  --ink:#1d2a30;
  --muted:#3f4c52;
  --white:#ffffff;
  --line:#2a6e88;
}
*{box-sizing:border-box;margin:0;padding:0}
html,body{width:1200px;height:3776px;overflow:hidden;background:var(--white)}
body{font-family:"Mulish",sans-serif;color:var(--ink);position:relative}
.abs{position:absolute}
h1,h2,h3,.head{font-family:"Archivo",sans-serif}

/* header */
.site-header{left:0;top:0;width:1200px;height:108px;background:var(--white)}
.brand{display:flex;align-items:center;gap:10px;font-family:"Archivo",sans-serif;font-weight:800;color:var(--teal);font-size:22px;letter-spacing:.5px}
.brand-square{width:22px;height:22px;background:var(--teal);border-radius:3px}
.nav{left:362px;top:30px;display:flex;gap:24px;font-size:14px;color:var(--ink)}
.nav a{color:inherit;text-decoration:none;padding:14px 0 10px}
.nav a.active{font-weight:800;color:var(--teal);border-top:2px solid var(--teal)}
.btn{display:inline-flex;align-items:center;justify-content:center;gap:8px;border-radius:6px;font-weight:700;text-decoration:none}
.btn-teal{background:var(--teal);color:var(--white)}
.btn-contact{left:797px;top:35px;width:103px;height:37px;font-size:14px;font-weight:600}
.btn-phone{left:910px;top:35px;width:142px;height:37px;font-size:14px;font-weight:600}

/* hero */
.hero{left:0;top:108px;width:1200px;height:565px;background:linear-gradient(100deg,#4a4e52 0%,#6d6a66 30%,#3c434a 55%,#22282e 75%,#2c3338 100%)}
.hero-title{left:740px;top:126px;font-size:34px;line-height:39px;font-weight:800;color:var(--white);letter-spacing:.3px}
.hero-title span{color:var(--accent)}
.hero-text{left:740px;top:300px;width:340px;font-size:18px;line-height:24px;color:var(--white);font-weight:600}
.hero-req{left:740px;top:409px;width:164px;height:44px;font-size:14px;border-radius:4px}
.hero-call{left:918px;top:409px;width:116px;height:44px;font-size:14px;border-radius:4px}

/* section badge */
.badge{height:42px;border:2px solid var(--teal);display:flex;align-items:center;padding:0 18px 0 30px;font-family:"Archivo",sans-serif;font-weight:700;font-size:18px;color:var(--teal);background:var(--white);letter-spacing:.3px}
.badge:before{content:"";position:absolute;left:6px;top:-8px;width:2px;height:56px;background:var(--teal)}
.badge:after{content:"";position:absolute;left:-8px;top:8px;width:26px;height:2px;background:var(--teal)}
.section-title{font-size:27px;font-weight:700;color:var(--teal);letter-spacing:.3px}

/* products */
.card{width:287px;height:325px;border:2px solid var(--teal);border-radius:8px;overflow:hidden;background:var(--white)}
.card.active{background:var(--teal);height:345px}
.card-img{height:200px}
.card h3{font-size:16px;font-weight:700;color:var(--teal);margin:24px 0 6px 30px}
.card.active h3{color:var(--white);margin-left:24px}
.card p{font-size:11px;line-height:15px;color:var(--muted);margin:0 20px 0 30px}
.card.active p{color:var(--white);margin-left:24px}
.read-more{display:inline-block;margin:14px 0 0 24px;background:var(--white);color:var(--teal);font-size:11px;font-weight:800;border-radius:14px;padding:6px 12px}
.arrow-btn{width:30px;height:30px;border:1.5px solid var(--muted);border-radius:6px;display:flex;align-items:center;justify-content:center}
.btn-view{left:508px;top:1241px;width:183px;height:43px;font-size:14px;border-radius:4px}

/* about */
.pale-block{background:var(--pale);border-radius:0 16px 16px 0}
.body-copy{font-size:13px;line-height:19.5px;color:var(--ink)}
.sub-title{font-size:18px;font-weight:700;color:var(--teal);line-height:24px}
.check-list{list-style:none;background:var(--pale);border-radius:8px;padding:16px 24px}
.check-list li{font-size:12px;line-height:24px;display:flex;align-items:center;gap:10px}

/* excellence */
.accordion-open{left:150px;top:2193px;width:420px;height:117px;border:1.5px solid var(--teal);border-radius:8px;padding:20px 24px}
.accordion-open h4{font-size:13px;font-weight:800;margin-bottom:10px}
.accordion-open p{font-size:11.5px;line-height:16px;color:var(--muted)}
.acc-row{left:150px;width:420px;height:58px;border-bottom:1.5px solid var(--teal);display:flex;align-items:center;justify-content:space-between;padding:0 24px;font-size:13px;font-weight:800}

/* why */
.feature{width:270px;display:flex;gap:16px}
.feature-icon{flex:0 0 60px;height:60px;background:var(--teal);border-radius:8px;display:flex;align-items:center;justify-content:center}
.feature h4{font-size:14px;font-weight:800;margin:2px 0 4px}
.feature p{font-size:12.5px;line-height:19px;color:var(--muted)}

/* testimonials */
.testimonials{left:0;top:2963px;width:1200px;height:467px;background:linear-gradient(180deg,#3e464b 0%,#2c3338 60%,#242b30 100%)}
.t-card{width:287px;height:220px;background:var(--white);border-radius:10px;padding:20px 24px}
.t-person{display:flex;gap:14px;align-items:center}
.avatar{width:44px;height:44px;border-radius:6px;background:linear-gradient(135deg,#8a8f94,#5f666b)}
.t-name{font-size:12px;font-weight:800}
.t-loc{font-size:12px}
.stars{margin:18px 0 10px;display:flex;gap:3px}
.t-card p{font-size:11px;line-height:15px;color:var(--muted)}
.arrow-light{border-color:var(--white)}

/* footer */
.site-footer{left:0;top:3430px;width:1200px;height:346px;background:var(--teal-dark);color:var(--white)}
.f-title{font-family:"Archivo",sans-serif;font-size:16px;font-weight:700;letter-spacing:.3px}
.f-item{font-size:12px;line-height:16px;display:flex;gap:16px;align-items:flex-start}
.f-menu a{display:block;color:var(--white);text-decoration:none;font-size:12px;line-height:21px}
.social{display:flex;gap:6px}
.social span{width:24px;height:24px;border-radius:50%;background:var(--white)}
.btn-enquiry{left:828px;top:3578px;width:217px;height:55px;background:var(--white);color:var(--teal);font-size:16px;font-weight:800;border-radius:6px;gap:18px}
</style>
</head>
<body>

<!-- Header -->
<header class="site-header abs">
  <div class="brand abs" style="left:150px;top:36px"><span class="brand-square"></span>WAYPOINT</div>
  <nav class="nav abs">
    <a class="active" href="#">Home</a>
    <a href="#">About Us</a>
    <a href="#">Kitchen Solutions</a>
    <a href="#">Products</a>
    <a href="#">Our Works</a>
  </nav>
  <a class="btn btn-teal btn-contact abs" href="#">Contact Us</a>
  <a class="btn btn-teal btn-phone abs" href="tel:5550142290">
    <svg width="16" height="16" viewBox="0 0 24 24" fill="none" stroke="#fff" stroke-width="2"><path d="M22 16.9v3a2 2 0 0 1-2.2 2 19.8 19.8 0 0 1-8.6-3.1 19.5 19.5 0 0 1-6-6A19.8 19.8 0 0 1 2.1 4.2 2 2 0 0 1 4.1 2h3a2 2 0 0 1 2 1.7c.1.9.4 1.8.7 2.7a2 2 0 0 1-.5 2.1L8 9.8a16 16 0 0 0 6 6l1.3-1.3a2 2 0 0 1 2.1-.4c.9.3 1.8.6 2.7.7a2 2 0 0 1 1.7 2z"/></svg>
    (555) 014 2290
  </a>
</header>

<!-- Hero -->
<section class="hero abs" role="img" aria-label="Technician in blue gloves servicing a commercial oven">
  <h1 class="hero-title abs">KEEPING YOUR<br><span>KITCHEN RUNNING,</span><br>ONE SERVICE<br>AT A TIME</h1>
  <p class="hero-text abs">Expert service for restaurant cooking equipment — reliable, fast, and trusted by commercial kitchens.</p>
  <a class="btn btn-teal hero-req abs" href="#">REQUEST SERVICE</a>
  <a class="btn btn-teal hero-call abs" href="#">CALL NOW</a>
</section>

<!-- Products -->
<div class="badge abs" style="left:502px;top:722px">OUR PRODUCTS</div>
<h2 class="section-title abs" style="left:0;width:1200px;text-align:center;top:800px">EXQUISITE SOLUTIONS FOR DISCERNING TASTES</h2>

<div class="arrow-btn abs" style="left:77px;top:1028px"><svg width="14" height="14" viewBox="0 0 14 14" fill="none" stroke="#3f4c52" stroke-width="1.6"><path d="M9 2 4 7l5 5"/></svg></div>
<div class="arrow-btn abs" style="left:1086px;top:1028px"><svg width="14" height="14" viewBox="0 0 14 14" fill="none" stroke="#3f4c52" stroke-width="1.6"><path d="m5 2 5 5-5 5"/></svg></div>

<article class="card active abs" style="left:150px;top:875px">
  <div class="card-img" role="img" aria-label="Stainless steel commercial kitchen line" style="background:linear-gradient(160deg,#c9c7c2,#7d7a75 60%,#4f4c48)"></div>
  <h3>COOKING EQUIPMENTS</h3>
  <p>Lorem ipsum dolor sit amet, consectetur adipiscing elit, sed do eiusmod tempor incididunt ut labore et dolore.</p>
  <span class="read-more">READ MORE</span>
</article>
<article class="card abs" style="left:456px;top:875px">
  <div class="card-img" role="img" aria-label="Steaming stainless steel cooking kettles" style="background:linear-gradient(170deg,#e6e6e4,#9ea0a0 55%,#55595b)"></div>
  <h3>STEAM COOKING EQUIPMENTS</h3>
  <p>Lorem ipsum dolor sit amet, consectetur adipiscing elit, sed do eiusmod tempor incididunt ut labore et dolore.</p>
</article>
<article class="card abs" style="left:764px;top:875px">
  <div class="card-img" role="img" aria-label="Stand mixer preparing dough" style="background:linear-gradient(160deg,#d7d8d8,#a7a9a8 55%,#6c6e6e)"></div>
  <h3>PREPARATION EQUIPMENTS</h3>
  <p>Lorem ipsum dolor sit amet, consectetur adipiscing elit, sed do eiusmod tempor incididunt ut labore et dolore.</p>
</article>

<a class="btn btn-teal btn-view abs" href="#">VIEW ALL PRODUCTS</a>

<!-- About -->
<div class="pale-block abs" style="left:0;top:1325px;width:387px;height:625px"></div>
<div class="abs" role="img" aria-label="Modern commercial kitchen with extraction hoods and cooking stations" style="left:151px;top:1372px;width:432px;height:535px;border-radius:8px;background:linear-gradient(180deg,#1e2428 0%,#3a4247 40%,#5c656a 70%,#2a3035 100%)"></div>

<div class="badge abs" style="left:627px;top:1377px">ABOUT US</div>
<h2 class="section-title abs" style="left:627px;top:1440px;line-height:36px">OUR PASSION FOR CULINARY<br>EXCELLENCE</h2>
<p class="body-copy abs" style="left:627px;top:1522px;width:430px">Lorem ipsum dolor sit amet, consectetur adipiscing elit, sed do eiusmod tempor incididunt ut labore et dolore magna aliqua exercitation ullamco laboris nisi ut Sed ut perspiciatis unde omnis iste natus error sit voluptatem accusantium doloremque laudantium, totam rem aperiam, eaque ipsa quae ab illo inventore.</p>
<h3 class="sub-title abs" style="left:628px;top:1643px">COMPREHENSIVE SOLUTIONS<br>FOR PROFESSIONAL KITCHENS</h3>
<ul class="check-list abs" style="left:629px;top:1704px;width:401px;height:196px">
  <li><svg width="16" height="10" viewBox="0 0 16 10" fill="none" stroke="#0e5672" stroke-width="1.4"><path d="M0 5h14M10 1l4 4-4 4"/></svg>International Kitchen Equipments</li>
  <li><svg width="16" height="10" viewBox="0 0 16 10" fill="none" stroke="#0e5672" stroke-width="1.4"><path d="M0 5h14M10 1l4 4-4 4"/></svg>Custom Equipment Designs</li>
  <li><svg width="16" height="10" viewBox="0 0 16 10" fill="none" stroke="#0e5672" stroke-width="1.4"><path d="M0 5h14M10 1l4 4-4 4"/></svg>Installation and Setup Services</li>
  <li><svg width="16" height="10" viewBox="0 0 16 10" fill="none" stroke="#0e5672" stroke-width="1.4"><path d="M0 5h14M10 1l4 4-4 4"/></svg>Maintenance and Support</li>
  <li><svg width="16" height="10" viewBox="0 0 16 10" fill="none" stroke="#0e5672" stroke-width="1.4"><path d="M0 5h14M10 1l4 4-4 4"/></svg>Consultation and Planning</li>
  <li><svg width="16" height="10" viewBox="0 0 16 10" fill="none" stroke="#0e5672" stroke-width="1.4"><path d="M0 5h14M10 1l4 4-4 4"/></svg>Inventory Management</li>
  <li><svg width="16" height="10" viewBox="0 0 16 10" fill="none" stroke="#0e5672" stroke-width="1.4"><path d="M0 5h14M10 1l4 4-4 4"/></svg>Kitchen accessories</li>
</ul>

<!-- Excellence -->
<div class="abs" style="left:790px;top:1953px;width:398px;height:587px;background:var(--pale);border-radius:16px 16px 0 0"></div>
<div class="abs" role="img" aria-label="Hand fitting a portafilter into a stainless espresso machine" style="left:630px;top:2000px;width:570px;height:463px;border-radius:8px 0 0 8px;background:linear-gradient(200deg,#4f5558 0%,#8d9395 35%,#c4a58c 60%,#6a6e70 85%)"></div>

<div class="abs" style="left:151px;top:2016px;display:flex;align-items:center;gap:18px;font-size:14px;font-weight:800">
  <svg width="50" height="50" viewBox="0 0 50 50"><circle cx="25" cy="25" r="24" fill="#e3eef1"/><circle cx="25" cy="25" r="18" fill="#0e5672"/><path d="M21 17v16l12-8z" fill="#fff"/></svg>
  Play Video
</div>
<h2 class="section-title abs" style="left:151px;top:2093px;line-height:38px">EXCELLENCE IN<br>KITCHEN SOLUTIONS</h2>

<div class="accordion-open abs">
  <h4>GLOBAL REACH</h4>
  <p>Lorem ipsum dolor sit amet, consectetur adipiscing elit, sed do eiusmod tempor incididunt ut labore et dolore magna aliqua exercitation ullamco</p>
  <svg class="abs" style="right:22px;top:20px" width="18" height="2"><rect width="18" height="2" fill="#1d2a30"/></svg>
</div>
<div class="acc-row abs" style="top:2322px">Customization and Design<svg width="18" height="18" viewBox="0 0 18 18" stroke="#1d2a30" stroke-width="2"><path d="M9 0v18M0 9h18"/></svg></div>
<div class="acc-row abs" style="top:2382px;border-bottom:none">Complete Support<svg width="18" height="18" viewBox="0 0 18 18" stroke="#1d2a30" stroke-width="2"><path d="M9 0v18M0 9h18"/></svg></div>

<!-- Why choose us -->
<div class="abs" style="left:0;top:2540px;width:1200px;height:423px;background:var(--pale)"></div>
<div class="abs" style="left:150px;top:2606px;width:296px;height:294px;border-radius:24px;background:var(--teal);display:flex;align-items:center;justify-content:center;font-family:'Archivo',sans-serif;font-weight:800;font-size:30px;color:var(--white)">WAYPOINT</div>

<div class="badge abs" style="left:512px;top:2608px">WHY CHOOSE US</div>
<h2 class="section-title abs" style="left:512px;top:2674px">EXPERTISE, QUALITY, AND INNOVATION</h2>

<div class="feature abs" style="left:512px;top:2745px">
  <div class="feature-icon"><svg width="34" height="34" viewBox="0 0 24 24" fill="none" stroke="#fff" stroke-width="1.5"><circle cx="12" cy="8" r="4"/><path d="M4 21c0-4 3.6-7 8-7s8 3 8 7"/><path d="m10 17 2 2 3-3"/></svg></div>
  <div><h4>Certified Technicians</h4><p>Lorem ipsum dolor sit amet, consecteturadipiscing el</p></div>
</div>
<div class="feature abs" style="left:799px;top:2745px">
  <div class="feature-icon"><svg width="34" height="34" viewBox="0 0 24 24" fill="none" stroke="#fff" stroke-width="1.5"><circle cx="12" cy="12" r="3"/><path d="M12 2v3M12 19v3M2 12h3M19 12h3M5 5l2 2M17 17l2 2M5 19l2-2M17 7l2-2"/></svg></div>
  <div><h4>Industry Expertise</h4><p>Lorem ipsum dolor sit amet, consecteturadipiscing el</p></div>
</div>
<div class="feature abs" style="left:512px;top:2840px">
  <div class="feature-icon"><svg width="34" height="34" viewBox="0 0 24 24" fill="none" stroke="#fff" stroke-width="1.5"><circle cx="14" cy="12" r="7"/><path d="M14 8v4l3 2M2 9h4M1 12h4M2 15h4"/></svg></div>
  <div><h4>Fast Response Times</h4><p>Lorem ipsum dolor sit amet, onsecteturadipiscing elit</p></div>
</div>
<div class="feature abs" style="left:799px;top:2840px">
  <div class="feature-icon"><svg width="34" height="34" viewBox="0 0 24 24" fill="none" stroke="#fff" stroke-width="1.5"><path d="M2 12l4-4 4 2 4-2 4 1 4 3M6 14l3 3 2-1 2 2 2-1 3 1 4-4"/></svg></div>
  <div><h4>Reliable, Long-Term</h4><p>Lorem ipsum dolor sit amet, onsecteturadipiscing elit</p></div>
</div>

<!-- Testimonials -->
<section class="testimonials abs" role="img" aria-label="Dimmed commercial kitchen interior background">
  <div class="abs" style="left:488px;top:56px;width:198px;height:42px;border:2px solid #fff;display:flex;align-items:center;justify-content:center;font-family:'Archivo',sans-serif;font-size:18px;color:#fff;font-weight:500;letter-spacing:.5px">TESTIMONIALS</div>
  <h2 class="section-title abs" style="left:0;width:1200px;text-align:center;top:128px;color:#fff">UNMATCHED QUALITY AND SERVICE</h2>
  <div class="arrow-btn arrow-light abs" style="left:81px;top:280px"><svg width="14" height="14" viewBox="0 0 14 14" fill="none" stroke="#fff" stroke-width="1.6"><path d="M9 2 4 7l5 5"/></svg></div>
  <div class="arrow-btn arrow-light abs" style="left:1089px;top:280px"><svg width="14" height="14" viewBox="0 0 14 14" fill="none" stroke="#fff" stroke-width="1.6"><path d="m5 2 5 5-5 5"/></svg></div>
</section>

<article class="t-card abs" style="left:150px;top:3160px">
  <div class="t-person"><div class="avatar" role="img" aria-label="Customer portrait"></div><div><div class="t-name">DANA WHITLOW</div><div class="t-loc">USA</div></div></div>
  <div class="stars"><svg width="96" height="16" viewBox="0 0 96 16" fill="#0e5672"><g id="s1"><path d="M8 0l2.4 5 5.6.6-4.2 3.8 1.2 5.6L8 12.2 3 15l1.2-5.6L0 5.6 5.6 5z"/></g><use href="#s1" x="19.5"/><use href="#s1" x="39"/><use href="#s1" x="58.5"/><use href="#s1" x="78"/></svg></div>
  <p>Lorem ipsum dolor sit amet, consectetur adipiscing elit, sed do eiusmod tempor incididunt ut labore et dolore magna aliqua exercitation ullamco laboris nisi ut Sed ut perspiciatis unde omnis iste natus error sit voluptatem accusantium</p>
</article>
<article class="t-card abs" style="left:458px;top:3160px">
  <div class="t-person"><div class="avatar" role="img" aria-label="Customer portrait"></div><div><div class="t-name">DANA WHITLOW</div><div class="t-loc">USA</div></div></div>
  <div class="stars"><svg width="96" height="16" viewBox="0 0 96 16" fill="#0e5672"><use href="#s1"/><use href="#s1" x="19.5"/><use href="#s1" x="39"/><use href="#s1" x="58.5"/><use href="#s1" x="78"/></svg></div>
  <p>Lorem ipsum dolor sit amet, consectetur adipiscing elit, sed do eiusmod tempor incididunt ut labore et dolore magna aliqua exercitation ullamco laboris nisi ut Sed ut perspiciatis unde omnis iste natus error sit voluptatem accusantium</p>
</article>
<article class="t-card abs" style="left:765px;top:3160px">
  <div class="t-person"><div class="avatar" role="img" aria-label="Customer portrait"></div><div><div class="t-name">DANA WHITLOW</div><div class="t-loc">USA</div></div></div>
  <div class="stars"><svg width="96" height="16" viewBox="0 0 96 16" fill="#0e5672"><use href="#s1"/><use href="#s1" x="19.5"/><use href="#s1" x="39"/><use href="#s1" x="58.5"/><use href="#s1" x="78"/></svg></div>
  <p>Lorem ipsum dolor sit amet, consectetur adipiscing elit, sed do eiusmod tempor incididunt ut labore et dolore magna aliqua exercitation ullamco laboris nisi ut Sed ut perspiciatis unde omnis iste natus error sit voluptatem accusantium</p>
</article>

<!-- Footer -->
<footer class="site-footer abs">
  <div class="abs" style="left:148px;top:70px;width:170px;text-align:center">
    <div style="width:44px;height:44px;background:#fff;border-radius:4px;margin:0 auto 40px"></div>
    <div class="head" style="font-size:22px;font-weight:700;letter-spacing:.5px">WAYPOINT</div>
    <div style="font-size:10px;letter-spacing:3px;margin-top:4px">RESTAURANT SERVICE</div>
  </div>
  <div class="abs" style="left:372px;top:50px;width:1.5px;height:160px;background:#fff;opacity:.6"></div>

  <div class="f-title abs" style="left:415px;top:52px">CONTACT US</div>
  <div class="f-item abs" style="left:417px;top:95px">
    <svg width="14" height="16" viewBox="0 0 24 24" fill="#fff"><path d="M12 2a7 7 0 0 0-7 7c0 5 7 13 7 13s7-8 7-13a7 7 0 0 0-7-7zm0 9.5A2.5 2.5 0 1 1 12 6.5a2.5 2.5 0 0 1 0 5z"/></svg>
    <span>420 Harbor Mill Rd. Suite 2-310<br>Brookfield, TN 37900</span>
  </div>
  <div class="f-item abs" style="left:417px;top:152px">
    <svg width="14" height="14" viewBox="0 0 24 24" fill="#fff"><path d="M22 16.9v3a2 2 0 0 1-2.2 2 19.8 19.8 0 0 1-8.6-3.1 19.5 19.5 0 0 1-6-6A19.8 19.8 0 0 1 2.1 4.2 2 2 0 0 1 4.1 2h3a2 2 0 0 1 2 1.7c.1.9.4 1.8.7 2.7a2 2 0 0 1-.5 2.1L8 9.8a16 16 0 0 0 6 6l1.3-1.3a2 2 0 0 1 2.1-.4c.9.3 1.8.6 2.7.7a2 2 0 0 1 1.7 2z"/></svg>
    <span>+1 555 014 2290</span>
  </div>
  <div class="f-item abs" style="left:417px;top:188px">
    <svg width="14" height="12" viewBox="0 0 24 20" fill="#fff"><path d="M0 2a2 2 0 0 1 2-2h20a2 2 0 0 1 2 2v.5L12 10 0 2.5zM0 5l12 7.5L24 5v13a2 2 0 0 1-2 2H2a2 2 0 0 1-2-2z"/></svg>
    <span>info@waypointservice.com</span>
  </div>

  <div class="f-title abs" style="left:665px;top:52px">MENU</div>
  <nav class="f-menu abs" style="left:665px;top:80px">
    <a href="#">Home</a><a href="#">About Us</a><a href="#">Kitchen Solutions</a><a href="#">Products</a><a href="#">Our Works</a><a href="#">Contact Us</a>
  </nav>

  <div class="f-title abs" style="left:825px;top:52px">FOLLOW US</div>
  <div class="social abs" style="left:826px;top:86px"><span></span><span></span><span></span><span></span><span></span></div>

  <div class="abs" style="left:150px;top:250px;width:902px;height:1.5px;background:#fff;opacity:.8"></div>
  <div class="abs" style="left:0;top:292px;width:1200px;text-align:center;font-size:12px">Copyright © 2025 All Rights Reserved</div>
</footer>
<a class="btn btn-enquiry abs" href="#">ENQUIRY NOW
  <svg width="30" height="14" viewBox="0 0 30 14" fill="none" stroke="#0e5672" stroke-width="2"><path d="M0 7h28M22 1l6 6-6 6"/></svg>
</a>

</body>
</html>
```